Valtoria - Managed Service Provider Brochure

Our company has launched a new division, a "Managed Service Provider (MSP)" division and we are looking for a new bifold brochure to market our company.
This new service provides our clients a vendor management solution to save money and control their procurement process. We would like to maintain the same color scheme of black and red as the core colors along our logo.
We have provided a recent powerpoint presentation done by our team containing the copy material that can be used for this project. We do not require the images stay the same so feel free to incorporate what works best in the design.
Thank you.
It Company

```html
<!DOCTYPE html>
<html lang="en">
<head>
<meta charset="utf-8">
<title>Valtoria MSP Brochure</title>
<link rel="stylesheet" href="https://fonts.googleapis.com/css2?family=Open+Sans:wght@300;400;600;700&display=swap">
<style>
:root{
  --red:#e8474b;
  --red-dark:#c93438;
  --ink:#2c2d31;
  --dark:#3b3c41;
  --dark-2:#55565c;
  --grey:#b9babd;
  --grey-light:#dcdcde;
  --paper-1:#f4f4f5;
  --paper-2:#ececed;
  --paper-3:#f1f1f2;
  --chart-blue:#2f63c9;
  --white:#ffffff;
}
*{box-sizing:border-box;margin:0;padding:0}
html,body{width:1200px;height:931px;overflow:hidden}
body{font-family:"Open Sans",Arial,sans-serif;color:var(--ink);background:#dfe3e8;position:relative}
.panel{position:absolute;top:0;width:400px;height:931px;overflow:hidden}
.panel-left{left:0;background:var(--paper-1)}
.panel-center{left:400px;background:var(--paper-2);box-shadow:inset 6px 0 10px -6px rgba(0,0,0,.18),inset -6px 0 10px -6px rgba(0,0,0,.18)}
.panel-right{left:800px;background:var(--paper-3)}
.abs{position:absolute}
.band{position:absolute;left:0;right:0;color:var(--white);font-weight:300;font-size:17px;display:flex;align-items:center;padding-left:24px;
  background:linear-gradient(90deg,var(--dark) 0%,var(--dark-2) 65%,#c9c9cc 100%)}
.band-red{background:var(--red)}
.band-light{background:linear-gradient(90deg,#c4c4c7,#d8d8da);color:var(--red);font-weight:400}
.tiny{font-size:5.6px;line-height:1.45}
.small{font-size:6.4px;line-height:1.45}
ul{list-style:none}
.dots li::before{content:"• ";}

/* process chevrons */
.step{position:absolute;width:68px}
.step-arrow{height:24px;background:var(--red);color:var(--white);font-size:6px;text-align:center;display:flex;align-items:center;justify-content:center;
  clip-path:polygon(0 0,88% 0,100% 50%,88% 100%,0 100%,10% 50%);padding:0 8px;line-height:1.2}
.step-body{margin-top:7px;height:118px;background:var(--dark);color:#e6e6e6;padding:6px 4px}
.step-body li{margin-bottom:3px}
.step-foot{margin-top:6px;height:24px;background:#c2c3c6;color:#fff;font-size:5.2px;display:flex;align-items:center;justify-content:center;text-align:center;padding:0 4px;line-height:1.2}

.sub-bar{position:absolute;height:10px;font-size:5.6px;color:#fff;display:flex;align-items:center;justify-content:center}
.frame{position:absolute;border:3px solid var(--chart-blue);background:#fff}
.frame-title{background:var(--chart-blue);color:#fff;font-size:6px;font-weight:700;font-style:italic;padding:1px 4px}

/* workflow grid */
.flow-box{position:absolute;height:34px;background:var(--dark);color:#fff;font-size:9.5px;text-align:center;display:flex;align-items:center;justify-content:center;line-height:1.2;border:1px solid #8a8b8f}

table{border-collapse:collapse;position:absolute}
.vendor-table td{font-size:5.4px;font-style:italic;color:#555;padding:3px 3px;vertical-align:middle;line-height:1.35}
.vendor-table tr:nth-child(odd) td{background:#dcdcde}
.vendor-table tr:nth-child(even) td{background:#efefef}
.vendor-table th{height:28px;font-size:5px;font-weight:400;color:#fff}
.savings-table th{height:18px;font-size:5.8px;font-weight:700;color:#fff}
.savings-table td{font-size:5.8px;padding:3px 4px;line-height:1.35;vertical-align:middle}
.savings-table tr:nth-child(odd) td{background:#d4d4d6}
.savings-table tr:nth-child(even) td{background:#ececed}
.savings-table td:nth-child(3){font-size:5.4px}

/* partnering */
.label-box{position:absolute;background:var(--dark);color:#fff;font-size:9px;display:flex;align-items:center;padding-left:12px}
.obj-red{position:absolute;background:var(--red);color:#fff;font-size:5.6px;text-align:center;display:flex;align-items:center;justify-content:center;line-height:1.2;height:22px}
.tab{position:absolute;top:0;height:22px;color:#fff;font-size:9px;display:flex;align-items:center;justify-content:center}
.red-list{color:var(--red);font-size:5.4px;line-height:1.48;font-style:italic}

.challenge li{position:relative;padding-left:13px;margin-bottom:8px;font-size:10px;line-height:1.2;color:#222}
.challenge li::before{content:"";position:absolute;left:0;top:3px;width:6px;height:6px;background:var(--red)}
.challenge span{display:block;font-size:9.6px;color:#333}
</style>
</head>
<body>

<!-- LEFT PANEL -->
<section class="panel panel-left">
  <div class="band" style="top:10px;height:54px;font-size:16px">Cost Savings Realized</div>

  <div class="step" style="left:18px;top:72px">
    <div class="step-arrow">Project Definition</div>
    <ul class="step-body tiny dots"><li>Define project charter</li><li>Stakeholder mapping and change plan</li><li>Qualify project scope and risk mitigation</li></ul>
    <div class="step-foot">Project Plan</div>
  </div>
  <div class="step" style="left:92px;top:72px">
    <div class="step-arrow">Solution Design</div>
    <ul class="step-body tiny dots"><li>Current state data collection</li><li>Process discovery</li><li>VMS tool selection</li><li>Process engineering</li><li>Solution modeling</li><li>Technology design</li><li>Rate card analysis</li></ul>
    <div class="step-foot">Solution Design &amp; Change Plan</div>
  </div>
  <div class="step" style="left:166px;top:72px">
    <div class="step-arrow">Execution</div>
    <ul class="step-body tiny dots"><li>Supplier onboard and training</li><li>VMS configure and test</li><li>Go live and rollout</li><li>Supplier consolidation and contracts</li><li>Tracking</li></ul>
    <div class="step-foot">Transition &amp; Go-Live Execution</div>
  </div>
  <div class="step" style="left:240px;top:72px">
    <div class="step-arrow">Control</div>
    <ul class="step-body tiny dots"><li>On-site launch and support</li><li>Performance monitoring</li><li>Operational and technology reviews</li><li>Change management activities</li></ul>
    <div class="step-foot">Operational Steady State</div>
  </div>
  <div class="step" style="left:314px;top:72px">
    <div class="step-arrow">Close</div>
    <ul class="step-body tiny dots"><li>Lessons learned collection</li><li>Final documentation completion</li><li>Program handoff and sign off</li></ul>
    <div class="step-foot">Project Closeout &amp; Sign Off</div>
  </div>

  <div class="band" style="top:304px;height:50px;font-size:16px">Discovery Session with Key Stakeholders</div>

  <ul class="abs tiny dots" style="left:16px;top:366px"><li>Tenure Policy</li><li>Requisition Approval</li><li>Background / Drug Screen</li><li>Rehire Policy</li><li>Independent Contractors</li><li>Travel / Expense</li></ul>
  <ul class="abs tiny dots" style="left:212px;top:366px"><li>Order Approval &amp; Distribution</li><li>On Boarding &amp; Off Boarding</li><li>Assignment Management</li><li>Evaluations</li><li>Time &amp; Expense Entry</li><li>Assignment Termination</li></ul>

  <div class="sub-bar" style="left:6px;width:200px;top:436px;background:var(--red)">Sourcing Workshop</div>
  <div class="sub-bar" style="left:206px;width:194px;top:436px;background:var(--dark)">Technology Workshop</div>
  <ul class="abs tiny dots" style="left:16px;top:452px"><li>Invoicing Processes &amp; Procedures</li><li>Invoice Design</li><li>Cost Codes / Code Validation</li><li>A/P Export</li></ul>
  <ul class="abs tiny dots" style="left:212px;top:452px"><li>Company Hierarchy</li><li>Configuration</li><li>System Users</li><li>System Sign On &amp; Passwords</li><li>Technology Compatibility</li><li>Security</li></ul>
  <div class="sub-bar" style="left:6px;width:394px;top:526px;background:var(--dark);font-style:italic">Communication &amp; Training Workshop</div>
  <ul class="abs tiny dots" style="left:116px;top:541px"><li>Communications / Change Management Plan</li><li>Communication Approval Process</li><li>Training Plan – Delivery Method, Timing, Location, etc.</li></ul>

  <div class="abs" style="left:12px;top:588px;width:382px;height:44px;background:#fff;box-shadow:0 1px 2px rgba(0,0,0,.15)"></div>
  <div class="abs" style="left:14px;top:586px;width:140px;height:46px;background:var(--red);color:#fff;font-size:12px;font-style:italic;display:flex;align-items:center;justify-content:center">Reporting Categories</div>
  <div class="abs small" style="left:165px;top:594px;font-style:italic;color:#777;display:grid;grid-template-columns:50px 48px 50px 50px;row-gap:6px">
    <span>Financials</span><span>Usage</span><span>Suppliers</span><span>Projects</span>
    <span>Expenses</span><span>Head Count</span><span>Tenure</span><span>Compliance</span>
  </div>

  <div class="frame" style="left:12px;top:640px;width:166px;height:128px">
    <div class="frame-title">Spend Summary Dashboard</div>
    <svg width="160" height="110" viewBox="0 0 160 110" role="img" aria-label="Spend summary charts">
      <rect x="80" y="4" width="76" height="100" fill="#f3f3f3"/>
      <rect x="84" y="12" width="40" height="5" fill="#e8474b"/><rect x="84" y="20" width="55" height="5" fill="#52b552"/><rect x="84" y="28" width="30" height="5" fill="#f2a93b"/>
      <rect x="84" y="46" width="48" height="5" fill="#e8474b"/><rect x="84" y="54" width="62" height="5" fill="#52b552"/><rect x="84" y="62" width="36" height="5" fill="#f2a93b"/>
      <rect x="84" y="80" width="44" height="5" fill="#52b552"/><rect x="84" y="88" width="58" height="5" fill="#f2a93b"/>
      <path d="M4 100 L4 78 L14 74 L22 80 L30 60 L38 70 L46 40 L52 66 L58 58 L64 72 L72 64 L76 100 Z" fill="#4f86d9"/>
    </svg>
  </div>
  <div class="frame" style="left:12px;top:774px;width:162px;height:136px">
    <div class="frame-title">Spend Summary Dashboard</div>
    <svg width="156" height="118" viewBox="0 0 156 118" role="img" aria-label="Spend table and charts">
      <g fill="#dfe7f3"><rect x="4" y="4" width="70" height="6"/><rect x="4" y="14" width="70" height="6"/><rect x="4" y="24" width="70" height="6"/><rect x="4" y="34" width="70" height="6"/></g>
      <rect x="4" y="4" width="70" height="3" fill="#3f8f3f"/>
      <rect x="4" y="60" width="70" height="50" fill="#fff" stroke="#ccc"/>
      <rect x="8" y="86" width="30" height="22" fill="#e23b3b"/><rect x="40" y="70" width="30" height="38" fill="#2f63c9"/>
      <path d="M82 60 L88 10 L96 40 L104 44 L112 48 L124 50 L148 52 L148 60 Z" fill="#4f86d9"/>
      <rect x="82" y="68" width="68" height="42" fill="#eef2f8"/>
    </svg>
  </div>
  <div class="frame" style="left:180px;top:778px;width:146px;height:132px">
    <div class="frame-title">Job Rate Summary Dashboard</div>
    <svg width="140" height="114" viewBox="0 0 140 114" role="img" aria-label="Job rate bar charts">
      <rect x="6" y="6" width="44" height="42" fill="#eef2f8"/>
      <rect x="70" y="8" width="20" height="40" fill="#e23b3b"/><rect x="94" y="14" width="20" height="34" fill="#2f63c9"/>
      <g><rect x="20" y="80" width="6" height="26" fill="#2f63c9"/><rect x="28" y="70" width="6" height="36" fill="#e23b3b"/><rect x="36" y="86" width="6" height="20" fill="#52b552"/><rect x="44" y="74" width="6" height="32" fill="#8e5bc4"/><rect x="52" y="64" width="6" height="42" fill="#2fb5c9"/><rect x="60" y="78" width="6" height="28" fill="#f2a93b"/><rect x="68" y="70" width="6" height="36" fill="#2f63c9"/><rect x="76" y="82" width="6" height="24" fill="#e23b3b"/><rect x="84" y="66" width="6" height="40" fill="#52b552"/><rect x="92" y="76" width="6" height="30" fill="#8e5bc4"/><rect x="100" y="72" width="6" height="34" fill="#2fb5c9"/><rect x="108" y="84" width="6" height="22" fill="#f2a93b"/></g>
      <line x1="16" y1="106" x2="120" y2="106" stroke="#999" stroke-width=".6"/>
    </svg>
  </div>

  <div class="abs" style="left:186px;top:652px;width:200px;height:110px;background:#fff;box-shadow:0 1px 3px rgba(0,0,0,.18)"></div>
  <div class="abs" style="left:218px;top:644px;width:152px;height:36px;background:var(--red);color:#fff;font-size:12px;font-style:italic;display:flex;align-items:center;justify-content:center">Key Features</div>
  <ul class="abs tiny dots" style="left:196px;top:690px;width:80px;font-style:italic;color:#555"><li>Personalized Dashboards</li><li style="margin-top:6px">Ad hoc Reporting</li><li style="margin-top:4px">Automatic Scheduling &amp; Delivery</li></ul>
  <ul class="abs tiny dots" style="left:288px;top:690px;width:90px;font-style:italic;color:#555"><li>Forecasting &amp; Planning Tools</li><li>Easy-to-use Interface</li><li>Easy-to-read Reports</li></ul>
</section>

<!-- CENTER PANEL -->
<section class="panel panel-center">
  <div class="band band-red" style="top:12px;height:62px;font-size:15px;padding-left:22px">Streamlined, Automated Workflow</div>

  <div class="flow-box" style="left:4px;top:82px;width:78px">Requisition &amp;<br>Approval</div>
  <div class="flow-box" style="left:86px;top:82px;width:80px">Sourcing &amp;<br>Screening</div>
  <div class="flow-box" style="left:170px;top:82px;width:84px">Selection &amp;<br>On- Boarding</div>
  <div class="flow-box" style="left:258px;top:82px;width:74px">Time &amp;<br>Expense</div>
  <div class="flow-box" style="left:44px;top:122px;width:82px">Invoicing &amp;<br>Payment</div>
  <div class="flow-box" style="left:130px;top:122px;width:82px">Reporting</div>
  <div class="flow-box" style="left:216px;top:122px;width:86px">Off-Boarding &amp;<br>Quality Reviews</div>

  <div class="abs" style="left:44px;top:168px;font-size:11.5px;font-weight:700;color:#222">Supports unique workflow processes for:</div>
  <ul class="abs" style="left:44px;top:188px;font-size:10.5px;line-height:1.3;color:#333">
    <li>.Traditional Temporary/Contract Staffing</li><li>.Temporary or Contract to Hire</li><li>.Independent Contractors</li><li>.Payrolled Workers</li><li>.Professional Services Consultants</li><li>.Direct Hire</li>
  </ul>

  <div class="band" style="top:310px;height:40px;font-size:14px">Vendor Management</div>

  <table class="vendor-table" style="left:0;top:358px;width:400px">
    <colgroup><col style="width:135px"><col style="width:135px"><col style="width:130px"></colgroup>
    <tr><th style="background:var(--dark)">Supplier<br>Selection</th><th style="background:var(--red)">Supplier Management</th><th style="background:var(--dark)">Supplier<br>Compliance</th></tr>
    <tr><td>Evaluate &amp; retain key supplier relationships</td><td>Train suppliers on requirements, workflow processes &amp; utilization of essential software</td><td>Manage &amp; maintain contracts</td></tr>
    <tr><td>Identify gaps in service coverage</td><td>Facilitate communications throughout the requisition and fulfillment processes</td><td>Maintain insurance certifications</td></tr>
    <tr><td>Facilitate supplier selection process, ensuring ability to meet client requirements</td><td>Provide helpdesk support services to address questions</td><td>Conduct periodic audit to ensure compliance with business requirements</td></tr>
    <tr><td>Establish &amp; execute contract agreements</td><td>Pay suppliers</td><td></td></tr>
    <tr><td style="height:24px"></td><td>Conduct regular business reviews with suppliers</td><td></td></tr>
  </table>

  <div class="band" style="top:600px;height:40px;font-size:14px">Cost Savings Realized</div>

  <table class="savings-table" style="left:0;top:690px;width:400px">
    <colgroup><col style="width:135px"><col style="width:135px"><col style="width:130px"></colgroup>
    <tr><th style="background:var(--dark)">Cost Savings Category</th><th style="background:var(--red)">Cost Savings Area</th><th style="background:var(--dark)">Assumptions</th></tr>
    <tr><td>Bill Rate Savings</td><td>Rate Standardization</td><td>•Establish competitive rate card by job title &amp; geography<br>•Consolidate supplier base to leverage best pricing</td></tr>
    <tr><td style="height:30px">Utilization Savings</td><td>Eliminate Unauthorized Usage</td><td>•Implement Approval hierarchy controls</td></tr>
    <tr><td style="height:30px">Productivity Improvement</td><td>Workflow Process Automation</td><td>•Implement &amp; Configure<br>•Internal resource re-deployment</td></tr>
    <tr><td style="height:22px">1099 Reclassification</td><td>Risk of Audit and Financial Exposure</td><td>•Implement 1099 Compliance Program</td></tr>
    <tr><td>Demand Management &amp; Right Skilling</td><td>Requisition Management</td><td>•MSP Validation of requested skill requirements &amp; job duties prior to bursting requisitions to suppliers</td></tr>
  </table>
  <div class="abs" style="left:44px;top:866px;width:156px;height:6px;background:var(--dark);color:#aaa;font-size:4px;text-align:center;line-height:6px">Estimated Cost Savings</div>
  <div class="abs" style="left:200px;top:866px;width:120px;height:6px;background:var(--red);color:#fff;font-size:4px;text-align:center;line-height:6px">Total</div>
</section>

<!-- RIGHT PANEL -->
<section class="panel panel-right">
  <div class="band" style="top:14px;height:58px;font-size:15px;background:linear-gradient(90deg,var(--dark),#46474c)">Power of Partnering</div>

  <div class="label-box" style="left:0;top:76px;width:100px;height:34px">VISION</div>
  <div class="abs" style="left:108px;top:80px;width:220px;font-size:6px;font-weight:700;line-height:1.3;color:#333">Together we create a custom and unique contingent labor management program for Customer. Combining world-class products and services, our proposed solution achieves critical business requirements.</div>
  <div class="abs" style="left:330px;top:76px;width:70px;height:34px;background:var(--red)"></div>

  <div class="abs" style="left:0;top:116px;width:100px;height:20px;font-size:6px;font-weight:700;padding-left:10px;display:flex;align-items:center;border-bottom:1px solid #999">STRATEGIC OBJECTIVES</div>
  <div class="obj-red" style="left:104px;top:114px;width:66px">World class products<br>and services</div>
  <div class="obj-red" style="left:174px;top:114px;width:66px">Implementation and<br>processes</div>
  <div class="obj-red" style="left:244px;top:114px;width:156px">Ongoing Training and<br>technical support</div>

  <ul class="abs tiny" style="left:14px;top:140px;font-style:italic;color:#555"><li>.Risk Mitigation</li><li>.Cost Control</li><li>.Talent Management</li></ul>
  <ul class="abs tiny" style="left:104px;top:138px;font-style:italic;color:#555"><li>.Compliance Analysis</li><li>.MSP Personnel</li><li>.VMS Software</li></ul>
  <ul class="abs tiny" style="left:174px;top:138px;font-style:italic;color:#555"><li>.Efficient Change Management</li><li>.Proven Methodology</li></ul>
  <ul class="abs tiny" style="left:264px;top:138px;font-style:italic;color:#555"><li>.Continuous Improvement</li><li>.Scalable and Flexible</li></ul>

  <div class="abs" style="left:0;top:178px;width:100px;height:34px;font-size:6px;font-weight:700;padding-left:10px;display:flex;align-items:center;border-top:1px solid #999;border-bottom:1px solid #999;line-height:1.2">HOW WE<br>MEASURE SUCCESS</div>
  <ul class="abs tiny" style="left:104px;top:180px;font-style:italic;color:#555"><li>.Scalable and Flexible</li><li>.Quarterly business reviews</li><li>.Measurable cost savings</li></ul>
  <ul class="abs tiny" style="left:174px;top:176px;font-style:italic;color:#555"><li>.Timely implementations</li><li>.Supplier management</li><li>.Talent management</li></ul>
  <ul class="abs tiny" style="left:264px;top:176px;font-style:italic;color:#555"><li>.Trained, motivated users</li><li>.Custom application development</li></ul>

  <div class="band band-light" style="top:238px;height:68px;align-items:flex-start;flex-direction:column;justify-content:center;padding-left:12px">
    <span style="font-size:14px">Comprehensive Workforce Management</span>
    <span style="font-size:7.5px;font-weight:700;color:#333">Daily Task Management</span>
  </div>

  <div class="abs" style="left:0;top:310px;width:400px;height:22px">
    <div class="tab" style="left:0;width:76px;background:var(--dark)">FINANCE</div>
    <div class="tab" style="left:78px;width:86px;background:var(--red)">SUPPLIER MGMT</div>
    <div class="tab" style="left:166px;width:76px;background:var(--dark)">RISK</div>
    <div class="tab" style="left:244px;width:86px;background:var(--red)">TECHNOLOGY</div>
  </div>

  <ul class="abs red-list" style="left:4px;top:336px"><li>.Standardize rates</li><li>.Aggressive discounts</li><li>.Invoice reduction</li><li>.Invoice consolidation</li><li>.Custom interface</li><li>.Reverse billing</li><li>.Payment to suppliers</li><li>.Tax filing/Global ICR</li><li>.Reporting</li><li>.Analytics</li></ul>
  <ul class="abs red-list" style="left:86px;top:336px"><li>.Contracts</li><li>.Administration</li><li>.Enforcement</li><li>.Monitor compliance</li><li>.Add service quality</li><li>.Diversity spending</li><li>.Supplier audits</li><li>.Supplier reviews</li><li>.Supplier sourcing</li><li>.Supplier monitoring</li></ul>
  <ul class="abs red-list" style="left:172px;top:334px"><li>.Worker classification</li><li>.Co-employment management</li><li>.Insurance coverage</li><li>.Workers' comp</li><li>.NDAs</li><li>.Right to work in country</li><li>.Pre-staffing process</li><li>.Systems security</li><li>.Facilities security</li><li>.IP content protect</li></ul>
  <ul class="abs red-list" style="left:254px;top:334px"><li>.System administration</li><li>.User IDs, passwords</li><li>.Business rules</li><li>.Business units/CC</li><li>.Approval authorities</li><li>.User training</li><li>.Program support</li><li>.New User setup</li><li>.Suppliers</li><li>.Service providers</li><li>.End users</li></ul>

  <div class="label-box" style="left:0;top:474px;width:76px;height:26px;font-size:9px">PROCESS</div>
  <ul class="abs red-list" style="left:86px;top:474px"><li>.Project classification</li><li>.Order distribution</li><li>.Candidate screening</li><li>.Rate structures</li></ul>
  <ul class="abs red-list" style="left:172px;top:474px"><li>.Candidate submittals</li><li>.Interview scheduling</li><li>.On-boarding</li><li>.Ongoing improvement</li></ul>
  <ul class="abs red-list" style="left:254px;top:474px"><li>.Off-boarding</li><li>.Performance surveys</li><li>.ATs / SLAs</li></ul>

  <div class="abs" style="left:0;top:548px;width:400px;height:56px;background:linear-gradient(90deg,#ececed,#d9d9db)"></div>
  <div class="abs" style="left:4px;top:562px;font-size:13px;color:var(--red)">Challenges in Contingent Staffing</div>
  <div class="abs" role="img" aria-label="Clipboard checklist icon" style="left:332px;top:528px;width:64px;height:76px;background:var(--red);border-radius:6px;transform:rotate(-18deg)"></div>

  <ul class="abs challenge" style="left:8px;top:628px;width:388px">
    <li>Decentralized selection &amp; management of Supplier<span>Lack of visibility &amp; control over contracts, pricing, performance</span></li>
    <li>No formal requisition approval process<span>Unauthorized spend across the company</span></li>
    <li>Time capture, Invoicing &amp; Payment Processes are manual<span>Time fraud, billing errors, lost invoices, and duplicate data entry</span></li>
    <li>No formal process for qualification of 1099 workers<span>Risk of audit and potential for significant financial exposure</span></li>
    <li>Reporting is a manual process<span>Headcount, Usage, Financial, Diversity, Performance – labor intensive, multiple sources for information</span><span>Produced after the fact – cannot be done in real-time</span></li>
    <li>Heavy demand on resources &amp; time consuming processes<span>Inability to focus on strategic business issues</span></li>
  </ul>
</section>

</body>
</html>
```